Business Card: RW Office Partners - Your tidy answer finder

Business Name: RW Office Partners
Website: www.rwofficepartners.com.au
Email: marisol@rwofficepartners.com.au
Mobile: 61 487 902 346
Facebook: @rwofficepartners
Instrgram: @rwofficepartners

Brading Colours:
HEX
#986474
#ddccd3
#7a8498
#c9d8e4
#000000
#ffffff

Tag Line: Your tidy answer finder

Link to DRAFT website:
https://helpdeskhub.sitebuilderx.com/rw-office-partners

About Page from the website:
My name is Marisol Bramwell, and I would love to assist you to become more productive in your day to day and achieve your business and personal goals.
My mission is to give you time, time to work on the important tasks of your business or to be able to spend more time with your family. I will take on the tasks you don’t have time for, don’t know well or simply don’t like to do.
I have an extensive background in Administration, Tender Coordination, Document Control, WHS and Quality Management working primarily in the Construction, Mining and Corporate World.
I am passionate about being organised, having order and making things in your life (and mine) easier! I love to watch something unfold and grow into something amazing! I am known for being the go-to problem solver, the organiser of all things, producing high standards of work even under pressure. I’m also a confident communicator, and I understand that you’re busy running your business.

Target Market(s)

Small to Medium Business who require assistance in their business by a virtual assistant.

Industry/Entity Type

Virtual Assistant

Contact Information for Business Card

Mobile: 61 487 902 346

Font styles to use
Sans Serif

Colors
ffffff

Requirements
Must have
• Branding Colours as outlined.
Contact Details as outlined.
Logo as provided.
Proper contact details - mobile, facebook, instragm, website.
Simple, Elegant, very clean looking.
Should not have
• Note cute with pictures.
Not too girly as still want to market to construction companies.

```html
<!DOCTYPE html>
<html lang="en">
<head>
<meta charset="utf-8">
<title>RW Office Partners – Business Card</title>
<link rel="stylesheet" href="https://fonts.googleapis.com/css2?family=Roboto:wght@300;400&display=swap">
<style>
  :root {
    --mauve: #986474;
    --blush: #ddccd3;
    --slate: #7a8498;
    --ink: #1e1e1e;
    --paper: #ffffff;
    --backdrop: #e3e3e3;
  }
  * { margin: 0; padding: 0; box-sizing: border-box; }
  html, body {
    width: 1051px; height: 1200px; overflow: hidden;
    background: var(--backdrop);
    font-family: "Roboto", Arial, sans-serif;
  }
  .card {
    position: absolute; left: 108px;
    width: 837px; height: 475px; overflow: hidden;
  }
  .card--front { top: 95px; background: var(--paper); }
  .card--back { top: 624px; background: var(--mauve); display: flex; align-items: center; justify-content: center; }
  .card__art { position: absolute; inset: 0; width: 100%; height: 100%; }
  .brand {
    position: absolute; left: 26px; top: 80px;
    display: flex; align-items: center; gap: 14px;
    color: var(--mauve); font-weight: 400; font-size: 38px; letter-spacing: 0.5px;
    white-space: nowrap;
  }
  .brand__mark { width: 18px; height: 18px; background: var(--mauve); }
  .tagline {
    position: absolute; left: 35px; top: 176px;
    color: var(--paper); font-weight: 300; font-size: 22px;
  }
  .contact { position: absolute; left: 444px; top: 272px; list-style: none; }
  .contact__item {
    display: flex; align-items: center; height: 34px;
    color: var(--ink); font-weight: 300; font-size: 20px;
  }
  .contact__icon { width: 22px; height: 22px; margin-right: 10px; flex: none; }
  .brand--reverse {
    position: static; color: var(--paper); font-size: 50px; gap: 18px;
  }
  .brand--reverse .brand__mark { background: var(--paper); width: 22px; height: 22px; }
</style>
</head>
<body>
  <section class="card card--front">
    <svg class="card__art" viewBox="0 0 837 475" aria-hidden="true">
      <rect x="0" y="0" width="837" height="50" fill="var(--mauve)"/>
      <polygon fill="var(--mauve)" points="0,160 470,160 180,475 0,475"/>
      <polygon fill="var(--blush)" points="470,160 510,160 220,475 180,475"/>
    </svg>

    <div class="brand"><span class="brand__mark"></span>RW Office Partners</div>
    <p class="tagline">Your tidy answer finder</p>

    <ul class="contact">
      <li class="contact__item">
        <svg class="contact__icon" viewBox="0 0 22 22" aria-hidden="true"><rect x="6" y="2" width="10" height="18" rx="1.5" fill="none" stroke="var(--mauve)" stroke-width="1.6"/><line x1="9" y1="17" x2="13" y2="17" stroke="var(--mauve)" stroke-width="1.4"/></svg>
        61 487 902 346
      </li>
      <li class="contact__item">
        <svg class="contact__icon" viewBox="0 0 22 22" aria-hidden="true"><rect x="1.5" y="5" width="19" height="12" fill="none" stroke="var(--mauve)" stroke-width="1.6"/><path d="M1.5,5 L11,12 L20.5,5 M1.5,17 L8.5,10.5 M20.5,17 L13.5,10.5" fill="none" stroke="var(--mauve)" stroke-width="1.4"/></svg>
        marisol@rwofficepartners.com.au
      </li>
      <li class="contact__item">
        <svg class="contact__icon" viewBox="0 0 22 22" aria-hidden="true"><g fill="none" stroke="var(--mauve)" stroke-width="1.4"><circle cx="11" cy="11" r="9"/><ellipse cx="11" cy="11" rx="4" ry="9"/><line x1="2" y1="11" x2="20" y2="11"/><path d="M3.5,6.5 H18.5 M3.5,15.5 H18.5"/></g></svg>
        www.rwofficepartners.com.au
      </li>
      <li class="contact__item">
        <svg class="contact__icon" viewBox="0 0 22 22" aria-hidden="true"><circle cx="11" cy="11" r="6" fill="var(--mauve)"/></svg>
        @rwofficepartners
      </li>
      <li class="contact__item">
        <svg class="contact__icon" viewBox="0 0 22 22" aria-hidden="true"><circle cx="11" cy="11" r="6" fill="var(--mauve)"/></svg>
        @rwofficepartners
      </li>
    </ul>
  </section>

  <section class="card card--back">
    <div class="brand brand--reverse"><span class="brand__mark"></span>RW Office Partners</div>
  </section>
</body>
</html>
```